Business Card Design Project

I own a dental practice and would like to use a logo that was recently designed to make business cards.
I am looking for a clean card with the following information on the card.

Halvorsen Dental Center (Using the logo)
Martin L. Halvorsen, D.D.S.
7234 Pinewick Ave. Suite B
Colorado Springs, CO 80547
(719) 482-6130
halvorsendentalcenter@mailbox-example.net
www.halvorsendentalcenter.example

Also a list of items on the back:
Services include

Family Dentistry
Cosmetic
Whitening
Tooth Colored Fillings
Crowns/Bridges
Implants/Tooth Replacement
Dentures
Root Canals
Updates

Just an FYI, I added an email address and website address.

I also added my Pic.  Please give designs with and without the pic

Thanks

Target Market(s)

20-70 U.S. Female that handles the household budget.

Industry/Entity Type

Dental

Requirements
Must have
• The logo is key. The color scheme of the logo is also key. The back of the business card should have the list of Dental Services offered at the practice. The front should be clean and professional looking. No cartoons. I will also include a picture of myself. I think that the final card may or may not include this picture, so the card designs should come with and without the picture. USE THE BLUE LOGO ONLY!!!
Should not have
• NO teeth should be on the card.

```html
<!DOCTYPE html>
<html lang="en">
<head>
<meta charset="utf-8">
<title>Halvorsen Dental Center – Business Cards</title>
<link rel="stylesheet" href="https://fonts.googleapis.com/css2?family=Source+Sans+3:wght@400;600;700&display=swap">
<style>
  :root {
    --backdrop: #ebe7e2;
    --card: #ffffff;
    --brand-brown: #6a5853;
    --brand-blue: #6f8f9e;
    --ink: #2b2b2b;
    --band-dark: #1f4756;
    --band-light: #8ea6b0;
    --swoosh-brown: #6e5d55;
    --photo-top: #c9b7ad;
    --photo-bottom: #22252c;
  }
  * { box-sizing: border-box; margin: 0; padding: 0; }
  html, body {
    width: 1200px; height: 720px; overflow: hidden;
    background: var(--backdrop);
    font-family: "Source Sans 3", "Myriad Pro", sans-serif;
    color: var(--ink);
  }
  .sheet { position: relative; width: 1200px; height: 720px; }

  .card {
    position: absolute;
    width: 561px; height: 320px;
    background: var(--card);
    border-radius: 18px;
    overflow: hidden;
    box-shadow: 0 1px 3px rgba(0,0,0,.18);
  }
  .card--photo { left: 28px; top: 27px; }
  .card--plain { left: 28px; top: 369px; height: 318px; }
  .card--services { left: 616px; top: 184px; }

  .swoosh { position: absolute; left: 0; top: 0; width: 100%; height: 100%; }

  .portrait {
    position: absolute; left: 0; top: 50px; width: 200px; height: 250px;
    background: linear-gradient(180deg, var(--photo-top) 0%, #8d7a73 35%, var(--photo-bottom) 70%);
  }

  /* Brand name block */
  .brand { position: absolute; display: flex; flex-direction: column; }
  .brand__row { display: flex; align-items: center; gap: 10px; }
  .brand__dot { width: 30px; height: 30px; border-radius: 50%; background: var(--brand-blue); flex: none; }
  .brand__name {
    font-weight: 600; font-size: 29px; line-height: 1.02;
    color: var(--brand-brown); letter-spacing: .3px;
  }
  .brand__tagline {
    margin-top: 6px; font-size: 13px; letter-spacing: 1.1px;
    color: var(--brand-brown); text-transform: uppercase;
  }
  .brand--right { right: 36px; top: 34px; align-items: flex-end; text-align: right; }
  .brand--center { left: 0; right: 0; align-items: center; text-align: center; }
  .card--plain .brand--center { top: 26px; }
  .card--services .brand--center { top: 34px; }

  /* Contact details */
  .contact { position: absolute; font-size: 14.5px; line-height: 1; }
  .contact__line { display: flex; align-items: center; gap: 6px; white-space: nowrap; }
  .contact--right { right: 36px; top: 155px; text-align: right; }
  .contact--right .contact__line { justify-content: flex-end; margin-bottom: 6px; }
  .contact--right .contact__address { margin-bottom: 4px; }
  .contact--right .contact__gap { height: 9px; }
  .contact--center { left: 0; right: 0; top: 164px; }
  .contact--center .contact__line { justify-content: center; font-size: 13.5px; margin-bottom: 10px; }
  .contact--center .contact__line--split { gap: 6px; }
  .contact--center .contact__sep { width: 8px; }

  .icon { width: 13px; height: 13px; flex: none; }

  .holder-name {
    position: absolute; color: #fff; font-weight: 700; font-size: 17px;
    white-space: nowrap;
  }
  .holder-name small { font-weight: 400; font-size: 12.5px; }
  .card--photo .holder-name { left: 25px; top: 289px; }
  .card--plain .holder-name { left: 0; right: 0; text-align: center; top: 289px; }

  /* Services */
  .services { position: absolute; left: 0; right: 0; top: 188px; text-align: center; }
  .services__title { font-size: 21px; font-weight: 600; color: var(--brand-blue); margin-bottom: 10px; }
  .services__row { display: flex; justify-content: center; gap: 8px; font-size: 16px; margin-bottom: 8px; white-space: nowrap; }
  .services__item { display: flex; align-items: center; gap: 3px; }
  .services__bullet { width: 7px; height: 11px; flex: none; }
</style>
</head>
<body>
<main class="sheet">

  <!-- Front with portrait -->
  <section class="card card--photo" aria-label="Business card front with portrait">
    <div class="portrait" role="img" aria-label="Portrait photo of Dr. Martin L. Halvorsen in a dark suit"></div>

    <div class="brand brand--right">
      <div class="brand__row">
        <span class="brand__dot"></span>
        <span class="brand__name">Halvorsen<br>Dental Center</span>
      </div>
      <span class="brand__tagline">Family • Cosmetic • Implants</span>
    </div>

    <div class="contact contact--right">
      <div class="contact__line contact__address">7234 Pinewick Ave. Suite B</div>
      <div class="contact__line contact__address">Colorado Springs, CO 80547</div>
      <div class="contact__gap"></div>
      <div class="contact__line">
        <svg class="icon" viewBox="0 0 16 16"><circle cx="8" cy="8" r="7" fill="none" stroke="var(--brand-brown)" stroke-width="1.3"/><path d="M5.5 4.5c-.8 2.5 1.5 6 4.5 7l1-1.5-1.6-1-.8.7c-1-.5-2-1.8-2.2-2.9l.9-.6-.7-1.8z" fill="var(--brand-brown)"/></svg>
        (719) 482-6130
      </div>
      <div class="contact__line">
        <svg class="icon" viewBox="0 0 16 16"><rect x="1.5" y="4" width="13" height="9" rx="1.5" fill="var(--brand-brown)"/><path d="M2 5l6 4.5L14 5" fill="none" stroke="#fff" stroke-width="1.2"/></svg>
        halvorsendentalcenter@mailbox-example.net
      </div>
      <div class="contact__line">
        <svg class="icon" viewBox="0 0 16 16"><circle cx="8" cy="8" r="6.5" fill="var(--brand-brown)"/><path d="M1.8 6h12.4M1.8 10h12.4" stroke="#fff" stroke-width="1"/></svg>
        www.halvorsendentalcenter.example
      </div>
    </div>

    <svg class="swoosh" viewBox="0 0 561 320" aria-hidden="true">
      <defs>
        <linearGradient id="bandA" x1="0" x2="1" y1="0" y2="0">
          <stop offset="0" stop-color="var(--band-dark)"/>
          <stop offset="1" stop-color="var(--band-light)"/>
        </linearGradient>
      </defs>
      <path d="M0,244 C180,304 420,310 561,276 L561,320 L0,320 Z" fill="url(#bandA)"/>
      <path d="M0,224 C170,284 380,300 480,291 C380,305 170,296 0,236 Z" fill="var(--swoosh-brown)"/>
    </svg>

    <p class="holder-name">Martin L. Halvorsen, <small>D.D.S.</small></p>
  </section>

  <!-- Front without portrait -->
  <section class="card card--plain" aria-label="Business card front">
    <div class="brand brand--center">
      <div class="brand__row">
        <span class="brand__dot"></span>
        <span class="brand__name">Halvorsen<br>Dental Center</span>
      </div>
      <span class="brand__tagline">Family • Cosmetic • Implants</span>
    </div>

    <div class="contact contact--center">
      <div class="contact__line">
        <svg class="icon" viewBox="0 0 16 16"><circle cx="8" cy="8" r="7" fill="none" stroke="var(--brand-brown)" stroke-width="1.3"/><path d="M5.5 4.5c-.8 2.5 1.5 6 4.5 7l1-1.5-1.6-1-.8.7c-1-.5-2-1.8-2.2-2.9l.9-.6-.7-1.8z" fill="var(--brand-brown)"/></svg>
        (719) 482-6130
      </div>
      <div class="contact__line contact__line--split">
        <svg class="icon" viewBox="0 0 16 16"><rect x="1.5" y="4" width="13" height="9" rx="1.5" fill="var(--brand-brown)"/><path d="M2 5l6 4.5L14 5" fill="none" stroke="#fff" stroke-width="1.2"/></svg>
        halvorsendentalcenter@mailbox-example.net
        <span class="contact__sep"></span>
        <svg class="icon" viewBox="0 0 16 16"><circle cx="8" cy="8" r="6.5" fill="var(--brand-brown)"/><path d="M1.8 6h12.4M1.8 10h12.4" stroke="#fff" stroke-width="1"/></svg>
        www.halvorsendentalcenter.example
      </div>
      <div class="contact__line">7234 Pinewick Ave. Suite B, Colorado Springs, CO 80547</div>
    </div>

    <svg class="swoosh" viewBox="0 0 561 318" aria-hidden="true">
      <defs>
        <linearGradient id="bandB" x1="0" x2="1" y1="0" y2="0">
          <stop offset="0" stop-color="var(--band-dark)"/>
          <stop offset="1" stop-color="var(--band-light)"/>
        </linearGradient>
      </defs>
      <path d="M0,230 C180,290 420,300 561,270 L561,318 L0,318 Z" fill="url(#bandB)"/>
      <path d="M0,210 C170,270 380,290 470,284 C380,298 170,284 0,222 Z" fill="var(--swoosh-brown)"/>
    </svg>

    <p class="holder-name">Martin L. Halvorsen, <small>D.D.S.</small></p>
  </section>

  <!-- Back: services -->
  <section class="card card--services" aria-label="Business card back with list of services">
    <div class="brand brand--center">
      <div class="brand__row">
        <span class="brand__dot"></span>
        <span class="brand__name">Halvorsen<br>Dental Center</span>
      </div>
      <span class="brand__tagline">Family • Cosmetic • Implants</span>
    </div>

    <div class="services">
      <h2 class="services__title">list of Services</h2>
      <div class="services__row">
        <span class="services__item"><svg class="services__bullet" viewBox="0 0 8 12"><path d="M4 0C7 3 8 8 4 12C0 8 1 3 4 0Z" fill="var(--brand-blue)"/></svg>Family Dentistry</span>
        <span class="services__item"><svg class="services__bullet" viewBox="0 0 8 12"><path d="M4 0C7 3 8 8 4 12C0 8 1 3 4 0Z" fill="var(--brand-blue)"/></svg>Cosmetic</span>
        <span class="services__item"><svg class="services__bullet" viewBox="0 0 8 12"><path d="M4 0C7 3 8 8 4 12C0 8 1 3 4 0Z" fill="var(--brand-blue)"/></svg>Whitening</span>
      </div>
      <div class="services__row">
        <span class="services__item"><svg class="services__bullet" viewBox="0 0 8 12"><path d="M4 0C7 3 8 8 4 12C0 8 1 3 4 0Z" fill="var(--brand-blue)"/></svg>Tooth Colored Fillings</span>
        <span class="services__item"><svg class="services__bullet" viewBox="0 0 8 12"><path d="M4 0C7 3 8 8 4 12C0 8 1 3 4 0Z" fill="var(--brand-blue)"/></svg>Crowns/Bridges</span>
      </div>
      <div class="services__row">
        <span class="services__item"><svg class="services__bullet" viewBox="0 0 8 12"><path d="M4 0C7 3 8 8 4 12C0 8 1 3 4 0Z" fill="var(--brand-blue)"/></svg>Implants/Tooth Replacement</span>
        <span class="services__item"><svg class="services__bullet" viewBox="0 0 8 12"><path d="M4 0C7 3 8 8 4 12C0 8 1 3 4 0Z" fill="var(--brand-blue)"/></svg>Dentures</span>
        <span class="services__item"><svg class="services__bullet" viewBox="0 0 8 12"><path d="M4 0C7 3 8 8 4 12C0 8 1 3 4 0Z" fill="var(--brand-blue)"/></svg>Root Canals</span>
      </div>
    </div>
  </section>

</main>
</body>
</html>
```